Business Card Needed for Crafter of Pottery, Jewelry and Artwork

Calling all designers in search of an artistic challenge.

I need a new business card design for my pottery, jewelry and artwork business, Woven Glass and Tide, based in Vancouver BC.

I would like a card that is bright and inviting and preferably incorporates my logo and a sample of photos of my work while having a clean fresh look. The following contact details would preferably be included on the card as well:
• Melinda Osgood
• Designer
• Phone: 604.555.0147
• Email: Designer@WovenGlassandTide.example
• Website: www.WovenGlassandTide.example
• Blog: www.KilnNotesDaily.example

The logo is attached in two color schemes in both Vector and Source formats. On past cards I’ve also included photos of my work. By including photos of the work the pieces are showcased and it catches people’s eye and prompts them to pick up the card and look at it more closely. For example, if I leave a stack in a coffee shop I want people to be drawn to the card, to pick it up and get a sense of the my product lines. Please feel free to pull photos of my work directly off of my website. If you need photos with higher pixels please let me know and I’ll email them directly to you. The website background is bffbda (191, 251, 218). I would like the business cards to match the feel of the website for consistency but the cards do not need to use the exact same colors. My website and current business card are predominantly turquoise shades. The background uses stripes provided by the website template. I don’t know the exact colors of the stripes.

My current business card is attached to show the use of photos in a design. Please note that I am not thrilled with my own design and am looking for variations and completely new designs. This example is not meant to be used as a template or starting point.

Here is some background surrounding my company:
WGT offers one of a kind jewelry, pottery, artwork and leather bags each designed with a twist. The pottery varies from rustic every day functional ware to raku artwork. The jewelry ranges from simple sterling every day pieces to multimedia pieces incorporating stone, metal, ceramics and fabric. The artwork is multimedia, typically acrylic paired with a natural element such as bark. All the bags are leather with reworked kimono fabric or patterned silk lining.

Feel free to check out my website to get a flavour for my work and the color scheme I've used on marketing materials so far. www.wovenglassandtide.example
Updates

Thank you to everyone who has submitted a design so far. I hope everyone has received some helpful feedback.

I'm going to post a survey to customers and friends asking for their votes. If you have new designs to submit please try to get them in by Saturday March 30 at noon so that I can include it in the survey launch.

Thank you

Target Market(s)

Females aged 25-65 interested in one of a kind functional pottery and jewelry.

Industry/Entity Type

Coffee Shop

Requirements
Must have
• Contact information, website, blog
Nice to have
• Logo, photos

```html
<!DOCTYPE html>
<html lang="en">
<head>
<meta charset="utf-8">
<title>Woven Glass and Tide — Business Card</title>
<link rel="stylesheet" href="https://fonts.googleapis.com/css2?family=Libre+Baskerville:wght@400;700&display=swap">
<style>
  :root {
    --teal: #17b3a3;
    --teal-deep: #109686;
    --teal-stripe: rgba(255,255,255,0.06);
    --navy: #2d2a7a;
    --ink: #2b2b2b;
    --paper: #ffffff;
    --paper-shade: #f1f3f2;
    --backdrop: #e6e8e7;
  }
  * { box-sizing: border-box; margin: 0; padding: 0; }
  html, body { width: 1200px; height: 1000px; overflow: hidden; }
  body {
    background: var(--backdrop);
    font-family: "Libre Baskerville", Georgia, serif;
    position: relative;
  }
  .card {
    position: absolute;
    width: 640px;
    height: 366px;
    border-radius: 4px;
    overflow: hidden;
    box-shadow: 0 10px 24px rgba(0,0,0,0.18);
  }
  /* Front */
  .card-front { left: 70px; top: 110px; background: linear-gradient(135deg, var(--paper), var(--paper-shade)); }
  .front-watermark {
    position: absolute; right: 40px; top: 10px; width: 250px; height: 230px;
    background: radial-gradient(circle, rgba(0,0,0,0.035), rgba(0,0,0,0) 70%);
  }
  .badge {
    position: absolute; left: 60px; top: 62px; width: 196px; height: 196px;
    border-radius: 50%; border: 4px solid var(--teal); background: var(--paper);
    display: flex; align-items: center; justify-content: center; text-align: center;
    box-shadow: inset 0 0 0 8px var(--paper), inset 0 0 0 9px rgba(23,179,163,0.25);
  }
  .badge-name {
    color: var(--navy); font-weight: 700; font-size: 19px; line-height: 1.25;
    letter-spacing: 1px; text-transform: uppercase; width: 140px;
  }
  .identity { position: absolute; left: 300px; top: 70px; }
  .person-name { color: var(--teal); font-size: 24px; letter-spacing: 1px; text-transform: uppercase; }
  .person-role { color: var(--ink); font-size: 15px; margin-top: 10px; }
  .contact-list { list-style: none; margin-top: 34px; }
  .contact-item { display: flex; align-items: center; gap: 12px; color: var(--ink); font-size: 12.5px; margin-bottom: 8px; }
  .contact-icon {
    width: 16px; height: 16px; border-radius: 50%; border: 1.5px solid var(--teal);
    display: flex; align-items: center; justify-content: center; flex: none;
  }
  .front-rule { position: absolute; left: 0; right: 0; bottom: 80px; height: 4px; background: var(--teal); }
  .front-band {
    position: absolute; left: 0; right: 0; bottom: 0; height: 72px; background: var(--teal);
    display: flex; align-items: center; justify-content: center;
  }
  .band-url { color: var(--paper); font-size: 19px; letter-spacing: 0.5px; }
  /* Back */
  .card-back {
    left: 490px; top: 530px;
    background:
      repeating-linear-gradient(90deg, var(--teal-stripe) 0 28px, transparent 28px 56px),
      linear-gradient(135deg, var(--teal), var(--teal-deep));
  }
  .card-back .badge { left: 232px; top: 70px; width: 200px; height: 200px; border-color: var(--navy); border-width: 3px; box-shadow: none; }
  .back-url { position: absolute; left: 34px; bottom: 26px; color: var(--paper); font-size: 17px; letter-spacing: 0.5px; }
</style>
</head>
<body>
  <section class="card card-front" aria-label="Business card front">
    <div class="front-watermark" role="img" aria-label="Faint decorative flourish"></div>
    <div class="badge"><span class="badge-name">Woven Glass and Tide</span></div>
    <div class="identity">
      <h1 class="person-name">Melinda Osgood</h1>
      <p class="person-role">Designer</p>
      <ul class="contact-list">
        <li class="contact-item">
          <span class="contact-icon"><svg width="8" height="8" viewBox="0 0 10 10"><path d="M2 1l2 2-1 1.5c.6 1.2 1.3 1.9 2.5 2.5L7 6l2 2-1.5 1.5C4 9 1 6 .5 2.5z" fill="#17b3a3"/></svg></span>
          604.555.0147
        </li>
        <li class="contact-item">
          <span class="contact-icon"><svg width="9" height="7" viewBox="0 0 10 8"><rect x="0.5" y="0.5" width="9" height="7" fill="none" stroke="#17b3a3"/><path d="M.5 .5L5 4.5 9.5 .5" fill="none" stroke="#17b3a3"/></svg></span>
          Designer@WovenGlassandTide.example
        </li>
        <li class="contact-item">
          <span class="contact-icon"><svg width="9" height="9" viewBox="0 0 10 10"><circle cx="5" cy="5" r="4.2" fill="none" stroke="#17b3a3"/><path d="M1 5h8M5 1c-2 2.5-2 5.5 0 8M5 1c2 2.5 2 5.5 0 8" fill="none" stroke="#17b3a3" stroke-width=".8"/></svg></span>
          www.KilnNotesDaily.example
        </li>
      </ul>
    </div>
    <div class="front-rule"></div>
    <div class="front-band"><span class="band-url">www.WovenGlassandTide.example</span></div>
  </section>

  <section class="card card-back" aria-label="Business card back">
    <div class="badge"><span class="badge-name">Woven Glass and Tide</span></div>
    <p class="back-url">www.WovenGlassandTide.example</p>
  </section>
</body>
</html>
```